Professional, elegant brochure for funeral home

We have a funeral home. We would like a 2 sided brochure. On one side will be 3 columns for our cremation options and on the other side would be 2-3 columns of our burial options. Would like to print it and also will be putting it on our website at www.Varnelhaven.com

Use as examples

https://www.brimtolgrace.com/pricing-and-resources/online-cremation-package-options

https://pelladinechapel.com/wp-content/uploads/Cremation-with-Ceremony-Plans.pdf

We only need a simple 1page (front and back brochure). Once we have decided on the designer I can provide the final content to be placed on the brochure.

Target Market(s)

We are family owned business so Something soft, inviting, personable and looks professionally done.

Industry/Entity Type

Funeral Home

Requirements
Must have
• Look professional. Easy to read
Nice to have
• Softer Muted comforting colors. No bright colors.

```html
<!DOCTYPE html>
<html lang="en">
<head>
<meta charset="utf-8">
<title>Varnel Haven Funeral Home – Cremation &amp; Burial Brochure</title>
<link rel="stylesheet" href="https://fonts.googleapis.com/css2?family=Marcellus+SC&family=Lato:ital,wght@0,400;0,700;1,400;1,700&display=swap">
<style>
:root{
  --blue:#1b6aad;
  --blue-dark:#155a95;
  --green:#9cc33b;
  --ink:#2a2a2a;
  --muted:#555;
  --paper:#ffffff;
  --backdrop:#e9eaec;
  --photo-grey:#d9dadc;
}
*{box-sizing:border-box;margin:0;padding:0}
html,body{width:1200px;height:900px;overflow:hidden}
body{background:var(--backdrop);font-family:"Lato",Arial,sans-serif;color:var(--ink);position:relative}
.page{position:absolute;top:58px;width:502px;height:710px;background:var(--paper);overflow:hidden;box-shadow:0 2px 10px rgba(0,0,0,.15)}
.page--cremation{left:97px}
.page--burial{left:628px}
.abs{position:absolute}
.photo{position:absolute}
.photo--mourner{left:300px;top:0;width:202px;height:340px;background:linear-gradient(180deg,#cfd0d3 0%,#e4e5e7 60%,rgba(255,255,255,0) 100%)}
.photo--blossom-left{left:0;top:580px;width:140px;height:130px;background:radial-gradient(ellipse at 40% 70%,#e4ead2 0%,#eef1e4 45%,rgba(255,255,255,0) 75%)}
.photo--flowers-top{left:270px;top:0;width:232px;height:270px;background:radial-gradient(ellipse at 55% 40%,#d6d7d9 0%,#e8e9ea 50%,rgba(255,255,255,0) 78%)}
.photo--blossom-small{left:0;top:660px;width:80px;height:50px;background:radial-gradient(ellipse at 40% 60%,#e2e8cf 0%,rgba(255,255,255,0) 75%)}

.hero-title{font-family:"Marcellus SC",Georgia,serif;line-height:1}
.hero-title__storied{left:131px;top:112px;font-size:27px;color:#4a4a4a;letter-spacing:1px}
.hero-title__ever{left:86px;top:138px;font-size:80px;color:var(--green)}
.hero-title__after{left:163px;top:202px;font-size:80px;color:var(--blue)}

.pill{position:absolute;display:flex;align-items:center;color:#fff;font-style:italic;font-weight:700;border-radius:10px}
.pill--green{background:var(--green)}
.pill--blue{background:var(--blue)}
.section-pill{left:101px;top:304px;width:304px;height:30px;border-radius:15px;justify-content:center;font-size:21px}
.option-pill{left:20px;width:116px;font-size:11.5px;line-height:1.25;padding:0 8px}
.option-pill--1{top:410px;height:50px}
.option-pill--2{top:477px;height:63px}
.option-pill--3{top:559px;height:48px;padding-left:18px}
.option-text{left:144px;width:338px;font-size:7.3px;font-style:italic;line-height:1.4;color:var(--muted);border-left:1px solid #c9c9c9;padding-left:8px}
.option-text--1{top:410px;height:50px}
.option-text--2{top:477px;height:63px}
.option-text--3{top:559px;height:48px}
.intro{left:25px;top:345px;width:455px;font-size:7.2px;font-style:italic;line-height:1.45;color:var(--muted);text-align:justify}

.brand-name{position:absolute;font-family:"Marcellus SC",Georgia,serif;color:var(--blue);font-size:15px;line-height:1.1;text-align:center}
.brand-name--left{left:140px;top:632px;width:130px}
.brand-name--right{left:30px;top:566px;width:130px}

.phone-bar{position:absolute;height:26px;display:flex;align-items:center;justify-content:center;color:#fff;font-style:italic;font-weight:700;font-size:16px;letter-spacing:.5px}
.phone-bar--left{left:295px;top:634px;width:207px;background:var(--green);border-radius:13px 0 0 13px}
.phone-bar--right{left:0;top:640px;width:222px;background:var(--blue);border-radius:0 13px 13px 0}
.site-url{position:absolute;font-style:italic;font-weight:700;font-size:10px;letter-spacing:2px;color:#333}
.site-url--left{left:333px;top:670px}
.site-url--right{left:48px;top:673px}

.burial-title{font-family:"Marcellus SC",Georgia,serif;line-height:1}
.burial-title__all{left:113px;top:48px;font-size:48px;color:var(--blue)}
.burial-title__about{left:70px;top:96px;font-size:48px;color:var(--green)}
.burial-title__burials{left:28px;top:140px;font-size:62px;color:var(--blue)}
.tagline{left:25px;top:212px;width:300px;font-size:14px;font-weight:700;font-style:italic;line-height:1.3;color:#222}
.lead{left:25px;top:256px;width:455px;font-size:11.6px;line-height:1.4;color:#333;text-align:justify}

.col-pill{height:47px;width:220px;justify-content:center;font-size:13.5px;border-radius:12px;text-transform:uppercase}
.col-pill--graveside{left:22px;top:350px}
.col-pill--committal{left:268px;top:350px}
.col-pill--immediate{left:268px;top:530px}
.col-sub{width:220px;font-size:9px;font-weight:700;font-style:italic;line-height:1.35;color:#222}
.col-sub--graveside{left:22px;top:410px;text-align:right}
.col-sub--committal{left:268px;top:410px}
.col-sub--immediate{left:268px;top:593px}
.col-body{font-size:7px;line-height:1.45;color:#444;text-align:justify}
.col-body--graveside{left:22px;top:455px;width:220px}
.col-body--committal{left:268px;top:454px;width:214px}
.col-body--immediate{left:264px;top:616px;width:222px}
</style>
</head>
<body>

<section class="page page--cremation">
  <div class="photo photo--mourner" role="img" aria-label="Soft faded photograph of a man kneeling in grief at a graveside"></div>
  <div class="photo photo--blossom-left" role="img" aria-label="Faded photograph of white blossoms and leaves"></div>

  <h1 class="hero-title">
    <span class="abs hero-title__storied">Storied</span>
    <span class="abs hero-title__ever">Ever</span>
    <span class="abs hero-title__after">After</span>
  </h1>

  <h2 class="pill pill--green section-pill">All About Cremation Services</h2>

  <p class="abs intro">Many people are choosing to cremate, but that doesn't mean they have to sacrifice the healing elements of a traditional burial. Let us help you create a memorial onsite—because it's helpful for many families to have a physical marker of remains. We can provide a range of flowers and décor accessories so you can honor your loved one. An onsite memorial becomes a place to commemorate a life and gather beyond the home, at a permanent and meaningful location. In addition, please know you can bring remains to the cemetery any time, even long after cremation. For more information about our cremation services in Maple Hollow, NY, please contact us today.</p>

  <div class="pill pill--blue option-pill option-pill--1">Funeral Service with Cremation as Final Disposition</div>
  <p class="abs option-text option-text--1">Similar to a traditional funeral service, the body of the deceased is placed in a cremation or rental casket for the funeral service. Cremation is performed after the service and the cremated remains are returned to the family. If you would like more information about our cremation services and options, please contact us today.</p>

  <div class="pill pill--green option-pill option-pill--2">FuneCommittal Servicesral Service with Cremation as Final Disposition</div>
  <p class="abs option-text option-text--2">This act can be an important way to begin to let go. And it can be a creative, thoughtful reflection of your loved one. From sending remains in to space to letting them go at sea, we can help you plan a unique way to memorialize a life through scattering cremated remains.</p>

  <div class="pill pill--blue option-pill option-pill--3">Ash Scattering</div>
  <p class="abs option-text option-text--3">A beautiful service that is held at the cemetery, following a funeral at mortuary chapel or your place of religious worship. Gather around your loved one's cremated remains to commemorate their life and honor the memories shared. This symbolic service is a beautiful step forward in the healing process, and can accompany many end of life options.</p>

  <div class="brand-name brand-name--left">Varnel Haven<br>Funeral Home</div>
  <div class="phone-bar phone-bar--left">(555) 014-2270</div>
  <div class="site-url site-url--left">www.Varnelhaven.com</div>
</section>

<section class="page page--burial">
  <div class="photo photo--flowers-top" role="img" aria-label="Faded photograph of a bouquet of flowers"></div>
  <div class="photo photo--blossom-small" role="img" aria-label="Faded photograph of blossoms"></div>

  <h1 class="burial-title">
    <span class="abs burial-title__all">All</span>
    <span class="abs burial-title__about">About</span>
    <span class="abs burial-title__burials">Burials</span>
  </h1>

  <p class="abs tagline">Traditional. Profound. Healing. Design a permanent resting place for your loved one</p>
  <p class="abs lead">Burials are a traditional memorial choice that give families a meaningful physical symbol to mark a loved one's resting place. At Varnel Haven Funeral Home we offer a broad range of burial options in Maple Hollow, NY, and we invite you to read about all that's possible. We're here to help you design a service and a physical memorial that will be a beautiful place to visit, forevermore.</p>

  <h2 class="pill pill--green col-pill col-pill--graveside">Graveside Funeral Services</h2>
  <p class="abs col-sub col-sub--graveside">Express the life of your loved one and create a place for family and friends to gather.</p>
  <p class="abs col-body col-body--graveside">We can help you design a meaningful and healing service to take place at the graveside. These services can take place outdoors or even inside a mausoleum. We'll guide you through the process of personalizing both the service and the site in multiple ways. Working with your Funeral Director, you can select readings, speakers and create spiritual moments. You can include military honors, masonic rites and religious leadership. When it comes to memorialization, we offer many options. Your selection may include a flat memorial, upright monument, ledger, mausoleum plate, memorial benches or private estates. We're here to share our expertise, with professionalism and compassion. Contact us with any questions you may have</p>

  <h2 class="pill pill--blue col-pill col-pill--committal">Committal Services</h2>
  <p class="abs col-sub col-sub--committal">A graveside service takes place after a funeral and can be a profound healing experience.</p>
  <p class="abs col-body col-body--committal">Funerals often take place at the mortuary chapel or at your place of religious worship. In that case, an interment and committal service can follow at the graveside. These are important gatherings to commemorate a life and mark the end of physical closeness. Family and friends gather to commit a loved one to the earth and say final farewells together. A committal service is symbolic and a helpful step in healing.</p>

  <h2 class="pill pill--green col-pill col-pill--immediate">Immediate Burials</h2>
  <p class="abs col-sub col-sub--immediate">Together with your funeral professional, we can guide you through all of the arrangements</p>
  <p class="abs col-body col-body--immediate">Burials are often an unexpected need, and we can handle every detail should this option make sense for you and your family. Please call us any time to discuss your needs. Our mission is to ease your burden.</p>

  <div class="brand-name brand-name--right">Varnel Haven<br>Funeral Home</div>
  <div class="phone-bar phone-bar--right">(555) 014-2270</div>
  <div class="site-url site-url--right">www.Varnelhaven.com</div>
</section>

</body>
</html>
```